BARRIER BANNER KTV

I am looking for a visual for a banner
3 meters long by 1 high.
In the same theme as the visual identity of the company.
As simple as possible without overloading

There must be the LOGO, the title VOLTARIS SERVICES TECHNIQUES

_________________________

I am looking for a visual for a banner (barrier banner)
3 meters long by 1 high.

AIR CONDITIONING HEATING VENTILATION
04 52 31 69 14

Font styles to use
Sans Serif

Colors
33b8a4
00a990
33a6d7
0493ce
3176b5
0355a3
ffffff

Requirements
Should not have
• No photo
No photo

```html
<!DOCTYPE html>
<html lang="fr">
<head>
<meta charset="utf-8">
<title>Barrier banner – KTV</title>
<link rel="stylesheet" href="https://fonts.googleapis.com/css2?family=Montserrat:wght@800&family=Roboto:wght@700&family=Roboto+Condensed:wght@700&display=swap">
<style>
  :root {
    --page-bg: #eeeeee;
    --banner-bg: #ffffff;
    --ink-dark: #2d3e4a;
    --roof-green: #33bb93;
    --band-start: #33b8a4;
    --band-end: #2188b0;
    --text-light: #ffffff;
  }
  html, body {
    margin: 0;
    width: 1054px;
    height: 1200px;
    overflow: hidden;
    background: var(--page-bg);
  }
  .stage {
    width: 1054px;
    height: 1200px;
    display: flex;
    align-items: center;
    justify-content: center;
  }
  .barrier-banner {
    display: block;
    width: 990px;
    height: 330px;
    background: var(--banner-bg);
    box-shadow: 0 8px 24px rgba(0, 0, 0, 0.22);
  }
  .roof-dark { fill: var(--ink-dark); }
  .roof-green { fill: var(--roof-green); }
  .brand-name {
    font-family: "Montserrat", sans-serif;
    font-weight: 800;
    fill: var(--ink-dark);
  }
  .company-title {
    font-family: "Roboto Condensed", sans-serif;
    font-weight: 700;
    fill: var(--ink-dark);
  }
  .services-band { fill: url(#bandGradient); }
  .services-text {
    font-family: "Montserrat", sans-serif;
    font-weight: 800;
    fill: var(--text-light);
  }
  .contact-text {
    font-family: "Roboto", sans-serif;
    font-weight: 700;
    fill: var(--ink-dark);
  }
  .contact-divider { fill: var(--ink-dark); }
</style>
</head>
<body>
<main class="stage">
  <svg class="barrier-banner" viewBox="0 0 930 310" xmlns="http://www.w3.org/2000/svg" aria-label="Bannière KTV – Voltaris Services Techniques">
    <defs>
      <linearGradient id="bandGradient" x1="0" y1="0" x2="1" y2="0">
        <stop offset="0" stop-color="#33b8a4"/>
        <stop offset="1" stop-color="#2188b0"/>
      </linearGradient>
    </defs>

    <polygon class="roof-dark" points="0,0 930,0 930,74 465,21 0,74"/>
    <polygon class="roof-green" points="62,65 465,2 872,65 465,21"/>

    <text class="brand-name" x="465" y="152" text-anchor="middle" font-size="124" textLength="218" lengthAdjust="spacingAndGlyphs">KTV</text>

    <text class="company-title" x="465" y="193" text-anchor="middle" font-size="36" textLength="586" lengthAdjust="spacingAndGlyphs">VOLTARIS SERVICES TECHNIQUES</text>

    <rect class="services-band" x="0" y="208" width="930" height="52"/>
    <text class="services-text" x="465" y="248" text-anchor="middle" font-size="38" textLength="851" lengthAdjust="spacingAndGlyphs">AIR CONDITIONING HEATING VENTILATION</text>

    <text class="contact-text" x="184" y="292" font-size="24" textLength="167" lengthAdjust="spacingAndGlyphs">04 52 31 69 14</text>
    <rect class="contact-divider" x="361" y="268" width="3" height="32"/>
    <text class="contact-text" x="372" y="292" font-size="24" textLength="375" lengthAdjust="spacingAndGlyphs">voltaris-services-techniques.fr</text>
  </svg>
</main>
</body>
</html>
```